Business letterhead and powerpoint template

Hi, I have recently started using a new logo (found through PixelGrove) and would now like to use that logo for letterheads and powerpoint.

Attached is the logo and one version of a brochure I have recently used.

Industry/Entity Type

Business

```html
<!DOCTYPE html>
<html lang="en">
<head>
<meta charset="utf-8">
<title>Halden Capital Letterhead</title>
<link href="https://fonts.googleapis.com/css2?family=Open+Sans:wght@400;600&display=swap" rel="stylesheet">
<style>
  :root {
    --paper: #ffffff;
    --ink: #231f20;
    --orange: #f15a24;
    --rule: #bdbdbd;
  }
  html, body {
    margin: 0;
    padding: 0;
    overflow: hidden;
    background: var(--paper);
  }
  .letterhead {
    position: relative;
    width: 933px;
    height: 1200px;
    overflow: hidden;
    background: var(--paper);
    font-family: "Open Sans", sans-serif;
    color: var(--ink);
  }
  .brand {
    position: absolute;
    left: 69px;
    top: 68px;
    display: flex;
    align-items: center;
    gap: 12px;
  }
  .brand-mark {
    width: 22px;
    height: 22px;
    background: var(--orange);
  }
  .brand-name {
    font-size: 34px;
    font-weight: 400;
    letter-spacing: 1px;
    color: var(--ink);
    line-height: 1;
  }
  .address {
    position: absolute;
    left: 663px;
    top: 68px;
    height: 43px;
    padding-left: 12px;
    padding-top: 3px;
    border-left: 1px solid var(--rule);
    font-size: 13.5px;
    line-height: 18px;
  }
  .footer-band {
    position: absolute;
    left: 0;
    top: 1000px;
    width: 933px;
    height: 200px;
  }
  .contact {
    position: absolute;
    right: 30px;
    top: 1097px;
    margin: 0;
    padding: 0;
    list-style: none;
    color: #fff;
    font-size: 13.5px;
    line-height: 23px;
    text-align: right;
  }
  .contact li {
    display: flex;
    justify-content: flex-end;
    align-items: center;
    gap: 5px;
  }
  .contact svg {
    width: 10px;
    height: 10px;
  }
</style>
</head>
<body>
<div class="letterhead">
  <header>
    <div class="brand">
      <span class="brand-mark"></span>
      <span class="brand-name">HALDEN CAPITAL</span>
    </div>
    <div class="address">
      Level 8 Suite 14 42 Harbour Lane<br>
      Northgate 2100 NSW Australia
    </div>
  </header>

  <svg class="footer-band" viewBox="0 0 933 200" role="img" aria-label="Orange footer band with a curved top edge">
    <path fill="var(--orange)" d="M0 180 C260 176 420 130 560 90 C680 58 820 48 933 46 L933 200 L0 200 Z"/>
  </svg>

  <ul class="contact">
    <li>
      <svg viewBox="0 0 10 10"><path fill="none" stroke="#fff" stroke-width="1.2" d="M2 1 L4 3 L3 4.5 Q4.5 6.5 5.5 7 L7 6 L9 8 L7.5 9.5 Q3 8.5 0.5 2.5 Z"/></svg>
      +61 (0)2 9471 3520
    </li>
    <li>
      <svg viewBox="0 0 10 10"><rect x="3" y="1" width="4" height="3" fill="#fff"/><rect x="1" y="4" width="8" height="4" fill="#fff"/></svg>
      +61 (0)2 9471 3599
    </li>
    <li>
      <svg viewBox="0 0 10 10"><circle cx="5" cy="5" r="4" fill="none" stroke="#fff" stroke-width="1"/><path stroke="#fff" stroke-width="0.8" fill="none" d="M1 5 H9 M5 1 V9"/></svg>
      www.haldencapital.com.au
    </li>
  </ul>
</div>
</body>
</html>
```